Campaign Flyer for a local election

Black and white election flyer

See information below to be included:

Re-elect Morton
Experienced Glenmoor Board Member
Experienced NYC Principal
Experienced leader

One Year Board Accomplishments:
-Installed New Park Lights (Bollards)
-Red Brick Road Repair Project
-Established Closer Ties with Our local precinct to frequently monitor the community with directed security patrols. Requested an increased police presence.
-Met with the 82nd Precinct Officials & Assemblywoman, Linda Marwick to discuss our security issues
- Focused on maintenance of streetlights to make brighter streets
-Negotiated Contract & Hired Our New Landscaper, Hollowfield Landscapers
-Major Homeowner Shrub Replacement Project
- Addressing Standing Water in our Park (Installed French Drain)
- Replaced and upgraded all 5 outdoor circuit breaker panels
-Write monthly community newsletters
-Sewer cleaning project (had all community catch basins cleaned)
-Carefully overseeing our new school project. Coordinating with the sponsor and the school directors
-Delivered a very healthy budget to the community
-Works closely with our committees
-Events: Zoo event, Petting Zoo, Outdoor Movie Night, Egg Hunt

It is my intent to seek re-election.
(Photo) Morton Velasquez
-Dedicated to improving our community
-Hard-working…He gets thing done!
-Trustworthy

. .

Please note, I am submitting new information under accomplishments. The list of accomplishments should be in the same sequence, starting with: Met with the 82nd Precinct....
Please carefully review.
----------------------------------------------------------------------------------------------------------------------------------------------------------------

Re-elect Morton
Experienced NYC Principal
Experienced leader

Last Year’s Board Accomplishments:

-Met with the 82nd Precinct Officials & Assemblywoman, Linda Marwick, to discuss our security issues. Requested increased police presence.
-Established a strong partnership with the 82nd precinct to frequently monitor the community with directed security patrols.
-Replaced all new park lights (Bollards) to make the park brighter
- Focused on maintenance of streetlights to make streets brighter
-‘Fixing Our Streets Project’ (Repaired all cracked/missing red bricks)
-Homeowner Shrub Replacement Project (Replaced hundreds of bushes)
- I write the monthly community newsletter
-Carefully overseeing our new school project. Coordinating with the sponsor and the school director
-Monitoring C of O’s and homeowners Insurance

(Photo) Morton Velasquez
-Hard-working! I get things done!
-Trustworthy

. .

Re-elect Morton
Experienced NYC Principal
Experienced leader

(Photo) Morton Velasquez
-Trustworthy

. .

Target Market(s)

A Community electing a Board Member

Industry/Entity Type

residential election

Requirements
Must have
• all black, white and grey print. Flyers will not be printed in color
Nice to have
• See the information in the attachment below containing all my accomplishments
Should not have
• color

```html
<!DOCTYPE html>
<html lang="en">
<head>
<meta charset="utf-8">
<title>Re-elect Morton – Campaign Flyer</title>
<link href="https://fonts.googleapis.com/css2?family=Archivo+Black&family=Archivo:wght@700;800&family=Barlow+Condensed:wght@500;600;700&family=Outfit:wght@400&display=swap" rel="stylesheet">
<style>
  :root {
    --ink: #231f20;
    --grey: #b3b3b3;
    --pill-border: #bdbdbd;
    --page: #c8c9c9;
    --paper: #ffffff;
    --text: #231f20;
  }
  * { margin: 0; padding: 0; box-sizing: border-box; }
  html, body { width: 970px; height: 1200px; overflow: hidden; background: var(--page); }
  .flyer {
    position: absolute; left: 82px; top: 77px; width: 807px; height: 1045px;
    background: var(--paper);
    box-shadow: 0 18px 22px rgba(0,0,0,0.35);
  }
  .header {
    position: absolute; left: 0; top: 0; width: 100%; height: 191px; background: var(--ink);
  }
  .title {
    position: absolute; left: 0; width: 100%; top: 20px; text-align: center;
    font-family: "Archivo Black", sans-serif; font-size: 76px; line-height: 1;
    color: var(--paper); letter-spacing: -0.5px;
  }
  .credentials {
    position: absolute; left: 78px; top: 120px; display: flex; gap: 14px;
  }
  .credential {
    width: 213px; height: 63px; border: 2.5px solid var(--pill-border); border-radius: 32px;
    display: flex; flex-direction: column; align-items: center; justify-content: center;
    color: var(--paper); font-family: "Barlow Condensed", sans-serif; line-height: 1.05;
  }
  .credential-label { font-weight: 700; font-size: 23px; letter-spacing: 0.3px; }
  .credential-role { font-weight: 500; font-size: 22px; }
  .rule-grey { position: absolute; left: 0; width: 100%; height: 6px; background: var(--grey); }
  .rule-ink { position: absolute; left: 0; width: 100%; height: 3px; background: var(--ink); }
  .portrait {
    position: absolute; left: 0; top: 199px; width: 441px; height: 657px;
    background: linear-gradient(180deg, #ebecec 0%, #d9dada 45%, #b7b7b7 70%, #2a2a2a 78%, #1e1e1e 100%);
  }
  .accomplishments {
    position: absolute; left: 476px; top: 213px; width: 320px; color: var(--text);
  }
  .acc-heading {
    font-family: "Archivo", sans-serif; font-weight: 800; font-size: 25px; line-height: 1.05;
  }
  .acc-heading strong {
    display: block; font-family: "Archivo Black", sans-serif; font-weight: 400; font-size: 24.5px;
  }
  .acc-list { list-style: none; margin-top: 15px; }
  .acc-list li {
    position: relative; padding-left: 19px; width: 300px;
    font-family: "Outfit", sans-serif; font-size: 13.4px; line-height: 17.2px; margin-bottom: 3.6px;
  }
  .acc-list svg { position: absolute; left: 0; top: 3px; width: 13px; height: 13px; }
  .footer {
    position: absolute; left: 0; top: 862px; width: 100%; height: 183px; background: var(--ink);
  }
  .intent {
    position: absolute; left: 118px; top: 13px; width: 569px; height: 42px;
    background: var(--grey); border-radius: 21px; text-align: center;
    font-family: "Archivo Black", sans-serif; font-size: 26px; line-height: 42px; color: var(--ink);
    letter-spacing: -0.3px;
  }
  .candidate-name {
    position: absolute; left: 50px; top: 91px; font-family: "Archivo Black", sans-serif;
    font-size: 36px; line-height: 50px; color: var(--paper); letter-spacing: -0.5px; white-space: nowrap;
  }
  .pointer { position: absolute; left: 413px; top: 86px; width: 21px; height: 60px; }
  .qualities { position: absolute; left: 444px; top: 73px; list-style: none; }
  .qualities li {
    position: relative; padding-left: 26px; height: 26px;
    font-family: "Barlow Condensed", sans-serif; font-weight: 500; font-size: 22px; line-height: 26px;
    color: var(--paper); white-space: nowrap;
  }
  .qualities svg { position: absolute; left: 0; top: 7.5px; width: 11px; height: 11px; }
</style>
</head>
<body>
<main class="flyer">
  <header class="header">
    <h1 class="title">Re-elect Morton</h1>
    <div class="credentials">
      <div class="credential"><span class="credential-label">EXPERIENCED</span><span class="credential-role">Glenmoor Board Member</span></div>
      <div class="credential"><span class="credential-label">EXPERIENCED</span><span class="credential-role">NYC Principal</span></div>
      <div class="credential"><span class="credential-label">EXPERIENCED</span><span class="credential-role">leader</span></div>
    </div>
  </header>
  <div class="rule-grey" style="top:191px"></div>
  <div class="rule-ink" style="top:197px"></div>

  <div class="portrait" role="img" aria-label="Black and white portrait photo of candidate Morton Velasquez"></div>

  <section class="accomplishments">
    <h2 class="acc-heading">One Year Board <strong>ACCOMPLISHMENTS:</strong></h2>
    <ul class="acc-list">
      <li><svg viewBox="0 0 13 13"><rect x="0.7" y="2" width="10" height="10" rx="1.5" fill="none" stroke="#555" stroke-width="1.2"/><path d="M3 6.8l2.3 2.3L12 1.8" fill="none" stroke="#555" stroke-width="1.8"/></svg>Installed New Park Lights (Bollards)</li>
      <li><svg viewBox="0 0 13 13"><rect x="0.7" y="2" width="10" height="10" rx="1.5" fill="none" stroke="#555" stroke-width="1.2"/><path d="M3 6.8l2.3 2.3L12 1.8" fill="none" stroke="#555" stroke-width="1.8"/></svg>Red Brick Road Repair Project</li>
      <li><svg viewBox="0 0 13 13"><rect x="0.7" y="2" width="10" height="10" rx="1.5" fill="none" stroke="#555" stroke-width="1.2"/><path d="M3 6.8l2.3 2.3L12 1.8" fill="none" stroke="#555" stroke-width="1.8"/></svg>Established Closer Ties with Our local precinct to frequently monitor the community with directed security patrols. Requested an increased police presence.</li>
      <li><svg viewBox="0 0 13 13"><rect x="0.7" y="2" width="10" height="10" rx="1.5" fill="none" stroke="#555" stroke-width="1.2"/><path d="M3 6.8l2.3 2.3L12 1.8" fill="none" stroke="#555" stroke-width="1.8"/></svg>Met with the 82nd Precinct Officials &amp; Assemblywoman, Linda Marwick to discuss our security issues</li>
      <li><svg viewBox="0 0 13 13"><rect x="0.7" y="2" width="10" height="10" rx="1.5" fill="none" stroke="#555" stroke-width="1.2"/><path d="M3 6.8l2.3 2.3L12 1.8" fill="none" stroke="#555" stroke-width="1.8"/></svg>Focused on maintenance of streetlights to make brighter streets</li>
      <li><svg viewBox="0 0 13 13"><rect x="0.7" y="2" width="10" height="10" rx="1.5" fill="none" stroke="#555" stroke-width="1.2"/><path d="M3 6.8l2.3 2.3L12 1.8" fill="none" stroke="#555" stroke-width="1.8"/></svg>Negotiated Contract &amp; Hired Our New Landscaper, Hollowfield Landscapers</li>
      <li><svg viewBox="0 0 13 13"><rect x="0.7" y="2" width="10" height="10" rx="1.5" fill="none" stroke="#555" stroke-width="1.2"/><path d="M3 6.8l2.3 2.3L12 1.8" fill="none" stroke="#555" stroke-width="1.8"/></svg>Major Homeowner Shrub Replacement Project</li>
      <li><svg viewBox="0 0 13 13"><rect x="0.7" y="2" width="10" height="10" rx="1.5" fill="none" stroke="#555" stroke-width="1.2"/><path d="M3 6.8l2.3 2.3L12 1.8" fill="none" stroke="#555" stroke-width="1.8"/></svg>Addressing Standing Water in our Park (Installed French Drain)</li>
      <li><svg viewBox="0 0 13 13"><rect x="0.7" y="2" width="10" height="10" rx="1.5" fill="none" stroke="#555" stroke-width="1.2"/><path d="M3 6.8l2.3 2.3L12 1.8" fill="none" stroke="#555" stroke-width="1.8"/></svg>Replaced and upgraded all 5 outdoor circuit breaker panels</li>
      <li><svg viewBox="0 0 13 13"><rect x="0.7" y="2" width="10" height="10" rx="1.5" fill="none" stroke="#555" stroke-width="1.2"/><path d="M3 6.8l2.3 2.3L12 1.8" fill="none" stroke="#555" stroke-width="1.8"/></svg>Write monthly community newsletters</li>
      <li><svg viewBox="0 0 13 13"><rect x="0.7" y="2" width="10" height="10" rx="1.5" fill="none" stroke="#555" stroke-width="1.2"/><path d="M3 6.8l2.3 2.3L12 1.8" fill="none" stroke="#555" stroke-width="1.8"/></svg>Sewer cleaning project (had all community catch basins cleaned)</li>
      <li><svg viewBox="0 0 13 13"><rect x="0.7" y="2" width="10" height="10" rx="1.5" fill="none" stroke="#555" stroke-width="1.2"/><path d="M3 6.8l2.3 2.3L12 1.8" fill="none" stroke="#555" stroke-width="1.8"/></svg>Carefully overseeing our new school project. Coordinating with the sponsor and the school directors</li>
      <li><svg viewBox="0 0 13 13"><rect x="0.7" y="2" width="10" height="10" rx="1.5" fill="none" stroke="#555" stroke-width="1.2"/><path d="M3 6.8l2.3 2.3L12 1.8" fill="none" stroke="#555" stroke-width="1.8"/></svg>Delivered a very healthy budget to the community</li>
      <li><svg viewBox="0 0 13 13"><rect x="0.7" y="2" width="10" height="10" rx="1.5" fill="none" stroke="#555" stroke-width="1.2"/><path d="M3 6.8l2.3 2.3L12 1.8" fill="none" stroke="#555" stroke-width="1.8"/></svg>Works closely with our committees</li>
      <li><svg viewBox="0 0 13 13"><rect x="0.7" y="2" width="10" height="10" rx="1.5" fill="none" stroke="#555" stroke-width="1.2"/><path d="M3 6.8l2.3 2.3L12 1.8" fill="none" stroke="#555" stroke-width="1.8"/></svg>Events: Zoo event, Petting Zoo, Outdoor Movie Night, Egg Hunt</li>
    </ul>
  </section>

  <div class="rule-grey" style="top:856px"></div>
  <footer class="footer">
    <p class="intent">It is my intent to seek re-election.</p>
    <p class="candidate-name">Morton Velasquez</p>
    <svg class="pointer" viewBox="0 0 21 60"><polygon points="0,0 21,30 0,60" fill="var(--grey)"/></svg>
    <ul class="qualities">
      <li><svg viewBox="0 0 11 11"><circle cx="5.5" cy="5.5" r="5.5" fill="#fff"/><path d="M4.3 3l2.6 2.5-2.6 2.5" fill="none" stroke="#231f20" stroke-width="1.6"/></svg>Dedicated to improving our community</li>
      <li><svg viewBox="0 0 11 11"><circle cx="5.5" cy="5.5" r="5.5" fill="#fff"/><path d="M4.3 3l2.6 2.5-2.6 2.5" fill="none" stroke="#231f20" stroke-width="1.6"/></svg>Hard-working…He gets thing done!</li>
      <li><svg viewBox="0 0 11 11"><circle cx="5.5" cy="5.5" r="5.5" fill="#fff"/><path d="M4.3 3l2.6 2.5-2.6 2.5" fill="none" stroke="#231f20" stroke-width="1.6"/></svg>Trustworthy</li>
    </ul>
  </footer>
</main>
</body>
</html>
```